Veltrano Community Development Planning New web site

Design a new web site. I have a budget of $1,500.00.
Attached on PowerPoint is a complete site plan. Home page and linked pages.
10 - 12 pages. All copy and photos will be supplied. (300dpi)
I have shown them the concept which they like.
No data bases required. Home page with animations dissolving.
They former web site has been taken down. They have been in business 30 years in New Jersey
Colors teal blues and greens
There will be a new logo)being designed)
The text in home page copy will give you a detailed story what they are all about.

files have been approved for Veltrano, Inc.   Tomas is the designer

Industry/Entity Type

Community

```html
<!DOCTYPE html>
<html lang="en">
<head>
<meta charset="utf-8">
<title>Veltrano Inc</title>
<link href="https://fonts.googleapis.com/css2?family=Varela+Round&family=Open+Sans:wght@400&display=swap" rel="stylesheet">
<style>
  :root {
    --green: #4aa014;
    --green-dark: #3f8c10;
    --white: #ffffff;
    --ink: #111111;
    --menu-text: #1a1a1a;
    --menu-rule: #e2e2e2;
    --cta: #eef000;
    --footer: #000000;
    --footer-text: #9a9a9a;
  }
  * { box-sizing: border-box; margin: 0; padding: 0; }
  html, body { width: 1200px; height: 716px; overflow: hidden; }
  body { position: relative; font-family: "Varela Round", sans-serif; background: #e9ecf2; }

  .hero-photo {
    position: absolute; inset: 0;
    background:
      radial-gradient(ellipse at 55% 45%, rgba(255,255,255,0.55), rgba(255,255,255,0) 60%),
      linear-gradient(120deg, #dfe3ee 0%, #f1f2f6 35%, #d9c2b0 55%, #eef0f5 75%, #cfd6e6 100%);
  }

  .site-nav {
    position: absolute; top: 0; left: 0; width: 1200px; height: 61px;
    background: var(--green);
  }
  .nav-item {
    position: absolute; top: 0; height: 61px; line-height: 61px;
    transform: translateX(-50%);
    color: var(--white); font-size: 16px; letter-spacing: 0.2px;
    text-shadow: 0 1px 2px rgba(0,0,0,0.35); white-space: nowrap;
  }
  .nav-divider { position: absolute; top: 0; width: 1px; height: 61px; background: var(--green-dark); }

  .dropdown {
    position: absolute; left: 481px; top: 61px; width: 234px; height: 137px;
    background: var(--white); box-shadow: 0 2px 6px rgba(0,0,0,0.2);
    padding: 14px 12px 0 16px;
    font-family: "Open Sans", sans-serif;
  }
  .dropdown::before {
    content: ""; position: absolute; top: -7px; left: 20px;
    border-left: 7px solid transparent; border-right: 7px solid transparent;
    border-bottom: 7px solid var(--white);
  }
  .dropdown-item {
    height: 28.5px; line-height: 28px; font-size: 12.5px; color: var(--menu-text);
    border-bottom: 1px solid var(--menu-rule);
  }
  .dropdown-item:last-child { border-bottom: none; }

  .brand-name {
    position: absolute; top: 228px; left: 0; width: 1200px; text-align: center;
    font-size: 62px; color: var(--green); letter-spacing: 1px;
  }
  .brand-rule { position: absolute; top: 340px; left: 408px; width: 384px; height: 1px; background: var(--white); }
  .brand-mark { position: absolute; top: 317px; left: 577px; }

  .hero-title {
    position: absolute; top: 388px; left: 0; width: 1200px; text-align: center;
    font-size: 44px; color: var(--white); letter-spacing: 1px;
    -webkit-text-stroke: 1px #222; text-shadow: 0 2px 3px rgba(0,0,0,0.3);
  }
  .hero-text {
    position: absolute; top: 456px; left: 0; width: 1200px; text-align: center;
    font-size: 22.5px; line-height: 29px; color: var(--ink);
  }
  .cta-button {
    position: absolute; left: 485px; top: 555px; width: 230px; height: 53px;
    background: var(--cta); border: 1px solid #222;
    display: flex; align-items: center; justify-content: center; gap: 8px;
    font-size: 17px; color: #222;
  }

  .site-footer {
    position: absolute; left: 0; top: 677px; width: 1200px; height: 39px; background: var(--footer);
  }
  .social-links { position: absolute; left: 44px; top: 10px; }
  .copyright {
    position: absolute; right: 44px; top: 0; line-height: 39px;
    font-family: "Open Sans", sans-serif; font-size: 11.5px; color: var(--footer-text);
  }
</style>
</head>
<body>
  <div class="hero-photo" role="img" aria-label="Photograph of hands drafting architectural floor plans with a pencil and ruler"></div>

  <nav class="site-nav">
    <span class="nav-item" style="left:104px">HOME</span>
    <span class="nav-divider" style="left:151px"></span>
    <span class="nav-item" style="left:245px">ABOUT COMPANY</span>
    <span class="nav-divider" style="left:339px"></span>
    <span class="nav-item" style="left:397px">SERVICES</span>
    <span class="nav-divider" style="left:458px"></span>
    <span class="nav-item" style="left:599px">HOUSING REHAB APPLICATION</span>
    <span class="nav-divider" style="left:740px"></span>
    <span class="nav-item" style="left:867px">AFFORDABLE APPLICATION</span>
    <span class="nav-divider" style="left:997px"></span>
    <span class="nav-item" style="left:1068px">CONTACT US</span>
  </nav>

  <div class="dropdown">
    <div class="dropdown-item">LAKEWOOD</div>
    <div class="dropdown-item">BRICK</div>
    <div class="dropdown-item">JACKSON</div>
    <div class="dropdown-item">WARREN</div>
  </div>

  <h1 class="brand-name">VELTRANO INC</h1>
  <div class="brand-rule"></div>
  <svg class="brand-mark" width="46" height="46" viewBox="0 0 46 46" aria-hidden="true">
    <circle cx="23" cy="23" r="22" fill="none" stroke="#fff" stroke-width="1.2"/>
  </svg>

  <h2 class="hero-title">CONDUCT PLACEMENT LOTTERIES</h2>
  <p class="hero-text">Explain implementation of a lottery and select applicants and<br>keep you out of that process</p>

  <div class="cta-button">CALL TO ACTION
    <svg width="10" height="12" viewBox="0 0 10 12" aria-hidden="true"><path d="M2 1.5 L7 6 L2 10.5" fill="none" stroke="#222" stroke-width="2.4"/></svg>
  </div>

  <footer class="site-footer">
    <svg class="social-links" width="66" height="19" viewBox="0 0 66 19" aria-hidden="true">
      <circle cx="9" cy="9.5" r="8.5" fill="none" stroke="#fff" stroke-width="1"/>
      <circle cx="32" cy="9.5" r="8.5" fill="none" stroke="#fff" stroke-width="1"/>
      <circle cx="55" cy="9.5" r="8.5" fill="none" stroke="#fff" stroke-width="1"/>
      <rect x="50.5" y="6.5" width="9" height="6" rx="1" fill="#fff"/>
    </svg>
    <span class="copyright">©2014</span>
  </footer>
</body>
</html>
```